Redesign of an insurance website

Attached is an insurance website that I need to redesign. Currently the website is too dark. I like for example www.brenvalo.com . Could you make the website lighter and change the structure a little so that it is more user friendly?

Industry/Entity Type

Insurance

Number of Pages Required

4 page

```html
<!DOCTYPE html>
<html lang="cs">
<head>
<meta charset="utf-8">
<title>KRYTONA.CZ – pojištění</title>
<link href="https://fonts.googleapis.com/css2?family=Raleway:wght@400;500;600;700&display=swap" rel="stylesheet">
<style>
:root{
  --red:#e8232f;
  --ink:#333333;
  --muted:#555555;
  --light:#f5f5f5;
  --footer:#1b1b1b;
  --footer-text:#9a9a9a;
  --white:#ffffff;
}
*{margin:0;padding:0;box-sizing:border-box}
html,body{width:743px;height:1200px;overflow:hidden;background:var(--white)}
body{position:relative;font-family:'Raleway',Arial,sans-serif;color:var(--ink)}
.abs{position:absolute}
.btn{position:absolute;background:var(--red);color:var(--white);font-size:10px;letter-spacing:.5px;display:flex;align-items:center;justify-content:center;text-transform:uppercase}

/* header */
.site-header{top:0;left:0;width:743px;height:43px;background:var(--white);box-shadow:0 1px 3px rgba(0,0,0,.12);z-index:2}
.brand{left:62px;top:11px;font-size:18px;font-weight:600;color:var(--ink);letter-spacing:.3px}
.main-nav{left:273px;top:16px;display:flex;gap:14px;font-size:9.5px;color:#666;text-transform:uppercase}
.main-nav .active{color:var(--ink);font-weight:600}
.header-register{left:592px;top:10px;width:90px;height:22px}

/* hero */
.hero{top:43px;left:0;width:743px;height:277px;background:linear-gradient(90deg,#f4f4f4 0%,#e9e9e9 45%,#bdbdbd 70%,#5a5f66 100%)}
.hero-title{left:60px;top:40px;font-size:19px;font-weight:700;color:#4a4a4a;line-height:23px;text-transform:uppercase}
.benefits{left:61px;top:96px;list-style:none;font-size:10.5px;color:#555}
.benefits li{height:21.3px;display:flex;align-items:center;gap:7px}
.hero-btn{left:61px;top:208px;width:88px;height:24px}
.dots{left:354px;top:251px;display:flex;gap:4px}
.dots span{width:9px;height:9px;border-radius:50%;background:#444}
.dots span.on{background:var(--red)}

/* intro */
.intro-photo{left:62px;top:354px;width:248px;height:152px;border:3px solid #ddd;background:linear-gradient(135deg,#d8d4cf,#b8b0a6 50%,#8a8f96)}
.intro-title{left:327px;top:370px;font-size:16px;font-weight:600;line-height:20px;color:var(--ink)}
.intro-title span{color:var(--red)}
.intro-text{left:327px;top:413px;width:355px;font-size:7.6px;line-height:12.8px;color:var(--muted)}
.intro-btn{left:327px;top:462px;width:107px;height:24px}

/* how it works */
.how-band{left:0;top:546px;width:743px;height:232px;background:linear-gradient(180deg,#e6e6e6 0%,#e4e6e8 55%,#c7dbe4 68%,#7fb0c8 100%)}
.how-box{left:0;top:583px;width:363px;height:158px;background:var(--red);color:var(--white);padding:22px 12px 0 61px}
.how-box h2{font-size:16px;font-weight:600;margin-bottom:6px}
.how-box p{font-size:7.6px;line-height:12.8px}

/* products */
.products-title{left:0;top:810px;width:743px;text-align:center;font-size:16px;font-weight:500}
.card{position:absolute;top:873px;width:143px;height:115px;background:var(--light);box-shadow:0 1px 3px rgba(0,0,0,.15);text-align:center}
.card .icon{position:absolute;left:45px;top:-26px;width:52px;height:52px;border-radius:50%;background:var(--white);border:1px solid #ddd;display:flex;align-items:center;justify-content:center}
.card h3{margin-top:41px;font-size:10.5px;font-weight:500;color:var(--red);text-transform:uppercase}
.card p{margin-top:6px;font-size:7.8px;line-height:11.5px;color:#444}
.card a{display:block;margin-top:5px;font-size:7.8px;color:#222;text-decoration:underline}
.arrows{left:355px;top:1014px;display:flex;gap:12px}

/* footer */
.site-footer{left:0;top:1068px;width:743px;height:132px;background:var(--footer);color:var(--footer-text)}
.footer-brand{left:62px;top:22px;font-size:17px;font-weight:600;color:var(--white)}
.footer-about{left:62px;top:48px;width:150px;font-size:7.6px;line-height:11.5px}
.footer-about u{color:#ccc}
.copyright{left:62px;top:100px;font-size:7.6px}
.footer-col{top:26px;font-size:7.8px}
.footer-col h4{color:#e6e6e6;font-weight:500;font-size:8.2px;margin-bottom:8px}
.footer-col li{list-style:none;line-height:13.5px}
.social li{display:flex;align-items:center;gap:8px;line-height:19px}
.social i{width:9px;height:9px;border-radius:50%;background:#777;display:inline-block}
.newsletter-input{left:539px;top:43px;width:120px;height:22px;background:#2c2c2c;font-size:7.8px;color:#aaa;padding:6px 10px}
.newsletter-send{left:659px;top:43px;width:23px;height:22px;background:var(--red);display:flex;align-items:center;justify-content:center}
.footer-register{left:592px;top:82px;width:90px;height:22px}
</style>
</head>
<body>

<header class="abs site-header">
  <div class="abs brand">KRYTONA.CZ</div>
  <nav class="abs main-nav">
    <span class="active">Dom</span><span>O nas</span><span>Caste dotazy</span><span>Kontakt</span><span>Prihlasit se</span>
  </nav>
  <div class="btn header-register">Registrovat</div>
</header>

<section class="abs hero" role="img" aria-label="Muž v obleku se dotýká virtuálního tlačítka pojištění">
  <h1 class="abs hero-title">Proc hledat pojisteni<br>pres krytona.cz?</h1>
  <ul class="abs benefits">
    <li><svg width="11" height="11" viewBox="0 0 11 11"><rect x=".7" y=".7" width="9.6" height="9.6" fill="none" stroke="#333" stroke-width="1.2"/><path d="M2.5 5.5l2.2 2.2L10 1.5" fill="none" stroke="#333" stroke-width="1.8"/></svg>Lorem Ipsum is simply dummy text of the printing</li>
    <li><svg width="11" height="11" viewBox="0 0 11 11"><rect x=".7" y=".7" width="9.6" height="9.6" fill="none" stroke="#333" stroke-width="1.2"/><path d="M2.5 5.5l2.2 2.2L10 1.5" fill="none" stroke="#333" stroke-width="1.8"/></svg>Lorem Ipsum is simply dummy text</li>
    <li><svg width="11" height="11" viewBox="0 0 11 11"><rect x=".7" y=".7" width="9.6" height="9.6" fill="none" stroke="#333" stroke-width="1.2"/><path d="M2.5 5.5l2.2 2.2L10 1.5" fill="none" stroke="#333" stroke-width="1.8"/></svg>Contrary to popular belief, Lorem Ipsum is not simply</li>
    <li><svg width="11" height="11" viewBox="0 0 11 11"><rect x=".7" y=".7" width="9.6" height="9.6" fill="none" stroke="#333" stroke-width="1.2"/><path d="M2.5 5.5l2.2 2.2L10 1.5" fill="none" stroke="#333" stroke-width="1.8"/></svg>It is a long established fact that a reader distracted</li>
    <li><svg width="11" height="11" viewBox="0 0 11 11"><rect x=".7" y=".7" width="9.6" height="9.6" fill="none" stroke="#333" stroke-width="1.2"/><path d="M2.5 5.5l2.2 2.2L10 1.5" fill="none" stroke="#333" stroke-width="1.8"/></svg>There are many variations of passages of Lorem Ipsum</li>
  </ul>
  <div class="btn hero-btn">Čitaj više</div>
  <div class="abs dots"><span class="on"></span><span></span><span></span></div>
</section>

<div class="abs intro-photo" role="img" aria-label="Tři kolegové v kanceláři si podávají ruce"></div>
<h2 class="abs intro-title">Uzavreli jste minulosti nevhodnou pojistku?<br><span>Zbavte se Ji!</span></h2>
<p class="abs intro-text">Lorem Ipsum je jednostavno probni tekst koji se koristi u tiskarskoj i slovoslagarskoj industriji. Lorem Ipsum postoji kao industrijski standard još od 16-og stoljeća, kada je nepoznati tiskar uzeo tiskarsku galiju slova i posložio ih da bi napravio knjigu s uzorkom tiska.</p>
<div class="btn intro-btn">Chci usetrit</div>

<section class="abs how-band" role="img" aria-label="Záchranný kruh plovoucí na hladině vody"></section>
<div class="abs how-box">
  <h2>Jak to funguje</h2>
  <p>Odavno je uspostavljena činjenica da čitača ometa razumljivi tekst dok gleda raspored elemenata na stranici. Smisao korištenja Lorem Ipsum-a jest u tome što umjesto 'sadržaj ovdje, sadržaj ovdje' imamo normalni raspored slova i riječi, pa čitač ima dojam da gleda tekst na razumljivom jeziku. Mnogi programi za stolno izdavaštvo i uređivanje web stranica danas koriste Lorem Ipsum kao zadani model teksta, i ako potražite 'lorem ipsum' na Internetu, kao rezultat dobit ćete mnoge stranice u izradi.</p>
</div>

<h2 class="abs products-title">Najdeme nejvhodnější pojištění</h2>

<article class="card" style="left:61px">
  <div class="icon"><svg width="26" height="26" viewBox="0 0 26 26"><path d="M7 12l2-5h8l2 5v5H7z" fill="#444"/><circle cx="9.5" cy="17.5" r="1.6" fill="#fff"/><circle cx="16.5" cy="17.5" r="1.6" fill="#fff"/><path d="M3 10v8l6 6M23 10v8l-6 6" fill="none" stroke="#444" stroke-width="2.4"/></svg></div>
  <h3>Auto pojištění</h3>
  <p>Lorem Ipsum je jednostavno<br>probni tekst koji.</p>
  <a>KLIKNĚTE ZDE</a>
</article>
<article class="card" style="left:220px">
  <div class="icon"><svg width="26" height="26" viewBox="0 0 26 26"><path d="M13 3L2 13h3v10h6v-7h4v7h6V13h3z" fill="#444"/></svg></div>
  <h3>Majitelé domů</h3>
  <p>Lorem Ipsum je jednostavno<br>probni tekst koji.</p>
  <a>KLIKNĚTE ZDE</a>
</article>
<article class="card" style="left:379px">
  <div class="icon"><svg width="26" height="26" viewBox="0 0 26 26"><path d="M7 5l12-2v21l-12-1z" fill="#444"/><path d="M10 8h6M10 11h6M10 14h6M10 17h6M10 20h6" stroke="#fff" stroke-width="1"/></svg></div>
  <h3>Pojištění nájemce</h3>
  <p>Lorem Ipsum je jednostavno<br>probni tekst koji.</p>
  <a>KLIKNĚTE ZDE</a>
</article>
<article class="card" style="left:538px">
  <div class="icon"><svg width="26" height="26" viewBox="0 0 26 26"><rect x="6" y="3" width="14" height="21" fill="#444"/><g fill="#fff"><rect x="8.5" y="6" width="3" height="3"/><rect x="14.5" y="6" width="3" height="3"/><rect x="8.5" y="11" width="3" height="3"/><rect x="14.5" y="11" width="3" height="3"/><rect x="8.5" y="16" width="3" height="3"/><rect x="14.5" y="16" width="3" height="3"/></g></svg></div>
  <h3>Pojištění bytů</h3>
  <p>Lorem Ipsum je jednostavno<br>probni tekst koji.</p>
  <a>KLIKNĚTE ZDE</a>
</article>

<div class="abs arrows">
  <svg width="10" height="16" viewBox="0 0 10 16"><path d="M8 2L2 8l6 6" fill="none" stroke="#555" stroke-width="2"/></svg>
  <svg width="10" height="16" viewBox="0 0 10 16"><path d="M2 2l6 6-6 6" fill="none" stroke="#e8232f" stroke-width="2"/></svg>
</div>

<footer class="abs site-footer">
  <div class="abs footer-brand">KRYTONA.CZ</div>
  <p class="abs footer-about">Lorem Ipsum je jednostavno probni tekst koji se koristi u tiskarskoj i slovoslagarskoj industriji...<u>Read More</u></p>
  <p class="abs copyright">© 2017 &nbsp;|&nbsp; All Rights Reserved.</p>
  <div class="abs footer-col" style="left:266px">
    <h4>Ochrana soukromí</h4>
    <ul><li>Dom</li><li>O Nas</li><li>Caste Dotazy</li><li>Kontakt</li><li>Prihlasit Se</li></ul>
  </div>
  <div class="abs footer-col social" style="left:402px">
    <h4>Sociální odkazy</h4>
    <ul><li><i></i>Kruh</li><li><i></i>Vlákno</li><li><i></i>Síť Plus</li></ul>
  </div>
  <div class="abs footer-col" style="left:539px"><h4>Objednejte náš Newsletter</h4></div>
  <div class="abs newsletter-input">Email</div>
  <div class="abs newsletter-send"><svg width="11" height="11" viewBox="0 0 11 11"><path d="M10 1L1 5l3 1.5L5 10l1.5-2.5z" fill="#fff"/></svg></div>
  <div class="btn footer-register">Registrovat</div>
</footer>

</body>
</html>
```